Redesign of my Homepage - Online resource for anyone to learn American Sign Language

I would like to have a new homepage design http://www.HandwiseLessons.example . My business is a website for anyone to learn American Sign Language. There are over 300 video lessons, with each lesson having 20 vocabulary words, retention exercises, 16,000 video dictionary etc. It is a very extensive site. It is a self paced website. If you need a log in to see what customers see, please let me know. I would like to keep the same color scheme. I want the website to look modern and clean. I want a fresh look! I want something that is easy to navigate, attracts customers, and easy to follow. I would like the final design to communicate that my website is for anyone to learn how to sign with this incredible program.

Target Market(s)

Students taking American Sign Language, Parents with Deaf children, future interpreters for the deaf, co-workers of the Deaf. Also, schools that offer American Sign Language (online schools, homeschools, etc. ).

Industry/Entity Type

Business

Number of Pages Required

1 page

Requirements
Must have
• My project must be very clean and clear. I want my homepage to show that this is a program for people to learn how American Sign Language.
Nice to have
• Not sure. Surprise me.

```html
<!DOCTYPE html>
<html lang="en">
<head>
<meta charset="utf-8">
<title>Handwise Lessons – Learn ASL Online</title>
<link href="https://fonts.googleapis.com/css2?family=Montserrat:wght@500;700&family=Open+Sans:wght@400;500;600;700&display=swap" rel="stylesheet">
<style>
  :root {
    --green: #3ccf4e;
    --black: #111111;
    --ink: #222222;
    --text: #333333;
    --footer-bg: #f4f4f4;
    --diamond: #c9c9c9;
    --rule: #c8c8c8;
    --white: #ffffff;
    --hero-a: #dfe6ec;
    --hero-b: #eef1f3;
    --hero-c: #e4ebe6;
  }
  * { box-sizing: border-box; margin: 0; padding: 0; }
  html, body { width: 976px; height: 1200px; overflow: hidden; }
  body { font-family: "Open Sans", Arial, sans-serif; color: var(--text); background: var(--white); position: relative; }

  .hero { position: absolute; left: 0; top: 0; width: 976px; height: 590px; }
  .hero-photo {
    position: absolute; inset: 0;
    background: linear-gradient(160deg, var(--hero-a) 0%, var(--hero-b) 55%, var(--hero-c) 100%);
  }

  .brand { position: absolute; left: 40px; top: 38px; display: flex; align-items: center; gap: 8px; }
  .brand-dot { width: 18px; height: 18px; border-radius: 50%; background: var(--green); }
  .brand-name { font-family: "Montserrat", sans-serif; font-weight: 700; font-size: 28px; color: var(--black); letter-spacing: -0.5px; line-height: 1; }

  .account { position: absolute; top: 28px; right: 38px; display: flex; align-items: center; gap: 16px; }
  .login { font-family: "Montserrat", sans-serif; font-weight: 700; font-size: 11px; color: var(--black); display: flex; align-items: center; gap: 3px; }
  .signup { background: var(--green); color: var(--white); font-family: "Montserrat", sans-serif; font-weight: 700; font-size: 9.5px; width: 86px; height: 20px; display: flex; align-items: center; justify-content: center; gap: 3px; }

  .main-nav { position: absolute; top: 68px; left: 0; width: 976px; height: 16px; font-family: "Open Sans", sans-serif; font-weight: 500; font-size: 10.8px; color: var(--ink); letter-spacing: .4px; }
  .main-nav span { position: absolute; top: 0; display: flex; align-items: center; gap: 5px; white-space: nowrap; }
  .nav-rule { position: absolute; left: 37px; top: 100px; width: 901px; height: 1px; background: #b9bfc4; }

  .hero-title { position: absolute; left: 0; width: 1020px; top: 246px; text-align: center; font-family: "Montserrat", sans-serif; font-weight: 700; font-size: 40px; line-height: 48px; color: var(--ink); }
  .hero-sub { position: absolute; left: 217px; top: 304px; width: 542px; height: 34px; background: rgba(255,255,255,.6); display: flex; align-items: center; justify-content: center; font-family: "Montserrat", sans-serif; font-weight: 500; font-size: 17px; color: var(--black); letter-spacing: .2px; }
  .cta { position: absolute; top: 359px; width: 169px; height: 45px; display: flex; align-items: center; justify-content: center; font-family: "Open Sans", sans-serif; font-weight: 600; font-size: 13px; color: var(--white); border-radius: 2px; }
  .cta-try { left: 314px; background: var(--black); }
  .cta-buy { left: 495px; background: var(--green); }

  .audiences { position: absolute; top: 649px; left: 0; width: 976px; }
  .audience { position: absolute; width: 260px; text-align: center; }
  .audience-kicker { font-size: 10.5px; line-height: 14px; color: var(--ink); letter-spacing: .3px; }
  .audience-title { font-family: "Montserrat", sans-serif; font-weight: 700; font-size: 24px; line-height: 30px; color: var(--black); margin-top: 8px; letter-spacing: .5px; }
  .audience-icon { width: 90px; height: 90px; border-radius: 50%; margin: 10px auto 0; background: #eeeeee; }
  .audience-text { font-size: 11.5px; line-height: 18px; color: var(--text); margin-top: 19px; }
  .read-more { font-size: 11.5px; font-weight: 600; color: var(--black); margin-top: 4px; }

  .site-footer { position: absolute; left: 0; top: 945px; width: 976px; height: 255px; background: var(--footer-bg); text-align: center; }
  .social { position: absolute; left: 405px; top: 31px; }
  .footer-about { position: absolute; left: 66px; top: 88px; width: 844px; font-size: 11px; line-height: 21px; color: var(--text); }
  .footer-rule { position: absolute; left: 260px; top: 164px; width: 442px; height: 1px; background: var(--rule); }
  .footer-links { position: absolute; left: 0; width: 976px; top: 177px; font-size: 11.5px; color: var(--text); }
  .copyright { position: absolute; left: 0; width: 976px; top: 198px; font-size: 11.5px; color: var(--text); }
</style>
</head>
<body>
  <header class="hero">
    <div class="hero-photo" role="img" aria-label="Bright office photo of students learning at laptops"></div>

    <div class="brand">
      <span class="brand-dot"></span>
      <span class="brand-name">Handwise</span>
    </div>

    <div class="account">
      <span class="login">
        <svg width="8" height="9" viewBox="0 0 8 9"><rect x="0" y="4" width="8" height="5" fill="#111"/><path d="M1.8 4V2.6a2.2 2.2 0 0 1 4.4 0V4" fill="none" stroke="#111" stroke-width="1.2"/></svg>
        Log In
      </span>
      <span class="signup">
        <svg width="7" height="8" viewBox="0 0 8 9"><rect x="0" y="4" width="8" height="5" fill="#fff"/><path d="M1.8 4V2.6a2.2 2.2 0 0 1 4.4 0V4" fill="none" stroke="#fff" stroke-width="1.2"/></svg>
        SIGN UP
      </span>
    </div>

    <nav class="main-nav">
      <span style="left:328px">HOME</span>
      <span style="left:388px">HOW IT WORKS <svg width="7" height="5" viewBox="0 0 7 5"><path d="M.5 .8 3.5 3.8 6.5 .8" fill="none" stroke="#222" stroke-width="1"/></svg></span>
      <span style="left:496px">GIFT CERTIFICATES</span>
      <span style="left:621px">CONTACT US</span>
      <span style="left:715px">GROUP RATE FORM</span>
      <span style="left:844px">TEACHER'S GUIDE</span>
    </nav>
    <div class="nav-rule"></div>

    <h1 class="hero-title">LEARN ASL ONLINE</h1>
    <p class="hero-sub">HOW TO LEARN ASL THROUGH VIDEO LESSONS ONLINE</p>
    <a class="cta cta-try">TRY IT FREE</a>
    <a class="cta cta-buy">BUY NOW</a>
  </header>

  <section class="audiences">
    <article class="audience" style="left:69px">
      <p class="audience-kicker">LEARNING</p>
      <h2 class="audience-title">COMMUNITY</h2>
      <div class="audience-icon" role="img" aria-label="Colourful icon of people joined in a circle" style="background:radial-gradient(circle,#9cc6e6 0%,#eeeeee 70%)"></div>
      <p class="audience-text">Anyone that has a passion to learn American<br>Sign Language (ASL)</p>
      <p class="read-more">Read More ›</p>
    </article>
    <article class="audience" style="left:342px">
      <p class="audience-kicker">HEARING PARENTS OF DEAF CHILDREN</p>
      <h2 class="audience-title">PARENTS</h2>
      <div class="audience-icon" role="img" aria-label="Icon of a parent and child" style="background:radial-gradient(circle,#c6dfa8 0%,#eeeeee 70%)"></div>
      <p class="audience-text">Learn to communicate more effectively<br>with your child</p>
      <p class="read-more">Read More ›</p>
    </article>
    <article class="audience" style="left:635px">
      <p class="audience-kicker">DEAF AND HARD OF HEARING</p>
      <h2 class="audience-title">STUDENTS</h2>
      <div class="audience-icon" role="img" aria-label="Icon of a student reading a book" style="background:radial-gradient(circle,#a8e0b0 0%,#eeeeee 70%)"></div>
      <p class="audience-text">Learn to tackle the challenges you faced<br>in the classroom</p>
      <p class="read-more">Read More ›</p>
    </article>
  </section>

  <footer class="site-footer">
    <svg class="social" width="142" height="36" viewBox="0 0 142 36" aria-label="Social links">
      <rect x="5" y="5" width="25" height="25" fill="var(--diamond)" transform="rotate(45 17.5 17.5)"/>
      <rect x="41" y="5" width="25" height="25" fill="var(--diamond)" transform="rotate(45 53.5 17.5)"/>
      <rect x="77" y="5" width="25" height="25" fill="var(--diamond)" transform="rotate(45 89.5 17.5)"/>
      <rect x="112" y="5" width="25" height="25" fill="var(--diamond)" transform="rotate(45 124.5 17.5)"/>
    </svg>
    <p class="footer-about">Handwise Lessons is a subscription based website for American Sign Language (ASL) video lessons. The content is for anyone who wishes to learn ASL, regardless of age. It has been designed to instruct deaf students, parents of deaf children, and the community-at-large. You may cancel your subscription at any time. All lessons are taught by Deaf experts of ASL</p>
    <div class="footer-rule"></div>
    <p class="footer-links">Contact Us | Our Mission | Terms &amp; Conditions HandwiseLessons</p>
    <p class="copyright">HandwiseLessons ©2017 All Rights Reserved</p>
  </footer>
</body>
</html>
```